Veteran Reserved Parking Sign 12x18

Steadfast Homefront Kin Alliance is looking to have a new Veteran Reserved Parking Sign designed. Included in the files are our current logo, the rectangle with the name on it. Also included is our Alt Square version that we will often use. There are several other signs that we kind of like as examples, not not asking for exactly like those, we want you to be creative and show us some new ideas. These are full sized parking signs, 12" wide X 18" height.

Target Market(s)

Veterans and Military Friendly Americans

Industry/Entity Type

Veteran Nonprofit

Font styles to use
Other font styles liked:
• Our logo uses the Franklin Heavy Gothic Font but you are not required to use that font in design.

Requirements
Must have
• Our logo needs to be on there and well as SHKA.ORG
Should not have
• CAN NOT Mention Brave Return Initiative or have black silhouettes similar to their logo. SHKA is NOT the same nonprofit.

```html
<!DOCTYPE html>
<html lang="en">
<head>
<meta charset="utf-8">
<title>Reserved Veteran Parking Sign – SHKA</title>
<link rel="stylesheet" href="https://fonts.googleapis.com/css2?family=Oswald:wght@600;700&family=Hind:wght@400;600;700&display=swap">
<style>
  :root {
    --backdrop: #d4d4d4;
    --sign-dark: #262626;
    --sign-mid: #333333;
    --ink-white: #ffffff;
    --accent-red: #ff0000;
    --flag-red: #e8312f;
    --flag-navy: #1f2d66;
    --brand-square: #1f3a7a;
  }
  html, body {
    margin: 0;
    padding: 0;
    width: 871px;
    height: 1200px;
    overflow: hidden;
    background: var(--backdrop);
  }
  .canvas {
    position: relative;
    width: 871px;
    height: 1200px;
  }
  .parking-sign {
    position: absolute;
    left: 35px;
    top: 33px;
    width: 800px;
    height: 1134px;
    display: block;
  }
  .headline {
    font-family: "Oswald", "Arial Narrow", sans-serif;
    font-weight: 700;
  }
  .headline--white { fill: var(--ink-white); }
  .headline--red { fill: var(--accent-red); }
  .tagline {
    font-family: "Hind", "Helvetica", sans-serif;
    font-weight: 400;
    fill: var(--ink-white);
  }
  .org-name, .org-web {
    font-family: "Hind", "Helvetica", sans-serif;
    font-weight: 700;
    fill: var(--ink-white);
  }
</style>
</head>
<body>
<main class="canvas">
  <svg class="parking-sign" viewBox="0 0 800 1134" xmlns="http://www.w3.org/2000/svg" aria-label="Reserved Veteran Parking sign">
    <defs>
      <clipPath id="sign-shape">
        <rect x="0" y="0" width="800" height="1134" rx="38" ry="38"/>
      </clipPath>
      <radialGradient id="board-tone" cx="0.5" cy="0.35" r="0.8">
        <stop offset="0" stop-color="var(--sign-mid)"/>
        <stop offset="1" stop-color="var(--sign-dark)"/>
      </radialGradient>
      <linearGradient id="flag-tone" x1="0" y1="0" x2="1" y2="0">
        <stop offset="0" stop-color="var(--flag-red)"/>
        <stop offset="0.28" stop-color="var(--flag-red)"/>
        <stop offset="0.33" stop-color="var(--flag-navy)"/>
        <stop offset="1" stop-color="var(--flag-navy)"/>
      </linearGradient>
    </defs>

    <g clip-path="url(#sign-shape)">
      <rect class="sign-board" x="0" y="0" width="800" height="1134" fill="url(#board-tone)"/>

      <text class="headline headline--white" x="107" y="196" font-size="150" textLength="592" lengthAdjust="spacingAndGlyphs">RESERVED</text>

      <g class="star-row" fill="var(--ink-white)">
        <polygon points="323,260 328,274 343,274 331,283 335,297 323,288 311,297 315,283 303,274 318,274"/>
        <polygon points="402,240 408,257 427,257 412,268 418,286 402,275 386,286 392,268 377,257 396,257"/>
        <polygon points="479,260 484,274 499,274 487,283 491,297 479,288 467,297 471,283 459,274 474,274"/>
      </g>

      <path class="title-frame" d="M269,276 H84 V765 H717 V276 H531" fill="none" stroke="var(--ink-white)" stroke-width="2"/>

      <text class="headline headline--red" x="112" y="498" font-size="200" textLength="578" lengthAdjust="spacingAndGlyphs">VETERAN</text>
      <text class="headline headline--white" x="130" y="668" font-size="172" textLength="552" lengthAdjust="spacingAndGlyphs">PARKING</text>

      <text class="tagline" x="133" y="729" font-size="33" textLength="543" lengthAdjust="spacing">Thank You for your Service</text>

      <g class="org-mark">
        <rect x="228" y="770" width="56" height="56" fill="var(--brand-square)"/>
        <text class="org-name" x="298" y="818" font-size="62" textLength="274" lengthAdjust="spacingAndGlyphs">SHKA</text>
        <text class="org-name" x="400" y="850" font-size="15" text-anchor="middle">Steadfast Homefront Kin Alliance</text>
      </g>

      <text class="org-web" x="400" y="888" font-size="21" text-anchor="middle" letter-spacing="1">SHKA.ORG</text>

      <path class="flag-band" role="img" aria-label="Draped American flag with red stripes and white stars on navy"
            d="M0,865 C100,870 180,930 238,975 C320,940 420,912 520,905 C640,900 740,910 800,915 L800,1134 L0,1134 Z"
            fill="url(#flag-tone)"/>
    </g>
  </svg>
</main>
</body>
</html>
```